PLOVA Business Card

Crestline Property Upgrades and Refits. I need a business card designed for this new high end renovation business. I would like the logo centered on the back side with the ABN (71 903 257 146) on the bottom right hand corner.

I would like the following information placed on the other side along with some customized pattern or design.

Patrick Delvane
Director
Phone: 1300 847 926
Fax: (02) 9415 6702
Website: www.plovabuilding.com.au
Email: p.delvane@plovabuilding.com.au
PO Box 87,
Kelwyn NSW 2091

(FB Logo) PLOVA - Crestline Property Upgrades and Refits

The final design should communicate professionalism and trust.

Back side background colour: white
Front side: Undecided

```html
<!DOCTYPE html>
<html lang="en">
<head>
<meta charset="utf-8">
<title>PLOVA Business Card</title>
<link rel="stylesheet" href="https://fonts.googleapis.com/css2?family=Cabin:wght@500;600;700&display=swap">
<style>
  :root {
    --brand-blue: #0b5089;
    --card-white: #ffffff;
    --ink-dark: #2f2f33;
    --backdrop: #eeeeec;
    --type: "Cabin", Arial, sans-serif;
  }
  * { box-sizing: border-box; margin: 0; padding: 0; }
  html, body {
    width: 1200px;
    height: 957px;
    overflow: hidden;
    background: var(--backdrop);
    font-family: var(--type);
  }
  .canvas { position: relative; width: 1200px; height: 957px; }

  .card {
    position: absolute;
    width: 581px;
    height: 359px;
    background: var(--card-white);
    box-shadow: 0 1px 3px rgba(0,0,0,0.12);
    overflow: hidden;
  }

  /* Front: contact side */
  .card-front { left: 186px; top: 78px; }
  .front-panel {
    position: absolute; left: 0; top: 0;
    width: 487px; height: 100%;
    background: var(--brand-blue);
    color: var(--card-white);
  }
  .person-name {
    position: absolute; left: 42px; top: 148px;
    font-size: 23px; font-weight: 600; letter-spacing: 0.2px;
  }
  .person-role {
    position: absolute; left: 42px; top: 178px;
    font-size: 18px; font-weight: 600;
  }
  .contact-list { position: absolute; left: 42px; top: 218px; list-style: none; }
  .contact-item {
    display: flex; align-items: center; gap: 8px;
    height: 23px;
    font-size: 14.5px; font-weight: 500;
  }
  .contact-item.group-gap { margin-top: 7px; }
  .contact-icon { width: 14px; height: 14px; flex: none; fill: var(--card-white); }

  .front-strip {
    position: absolute; left: 487px; top: 0;
    width: 94px; height: 100%;
    display: flex; align-items: center; justify-content: center;
  }
  .front-strip .brand-name {
    transform: rotate(-90deg);
    font-size: 50px; font-weight: 700; color: var(--brand-blue);
    letter-spacing: 1px;
  }

  /* Back: logo side */
  .card-back { left: 456px; top: 529px; }
  .back-band {
    position: absolute; left: 0; top: 0;
    width: 59px; height: 100%;
    background: var(--brand-blue);
  }
  .back-logo {
    position: absolute; left: 59px; right: 0; top: 118px;
    text-align: center;
  }
  .back-logo .brand-name {
    display: block;
    font-size: 66px; font-weight: 700; color: var(--brand-blue);
    letter-spacing: 3px; line-height: 1;
  }
  .tagline {
    display: flex; align-items: center; justify-content: center; gap: 6px;
    margin-top: 16px;
    font-size: 15.5px; font-weight: 500; color: var(--brand-blue);
    letter-spacing: 0.6px; text-transform: uppercase;
  }
  .tagline-rule { width: 32px; height: 1.5px; background: var(--brand-blue); }
  .abn {
    position: absolute; right: 22px; bottom: 22px;
    font-size: 15px; font-weight: 600; color: var(--brand-blue);
  }
</style>
</head>
<body>
<div class="canvas">

  <section class="card card-front">
    <div class="front-panel">
      <h1 class="person-name">Patrick Delvane</h1>
      <p class="person-role">Director</p>
      <ul class="contact-list">
        <li class="contact-item">
          <svg class="contact-icon" viewBox="0 0 16 16"><path d="M3.6 1.2l2.3 2.6-1.3 1.8c.9 2 2.6 3.7 4.6 4.6l1.8-1.3 2.6 2.3-1.2 2.4C7 13.4 2.6 9 1.2 2.4z"/></svg>
          <span>1300 847 926</span>
        </li>
        <li class="contact-item">
          <svg class="contact-icon" viewBox="0 0 16 16"><path d="M4 1h8v4H4zM1 6h14v6h-3v3H4v-3H1zm4 4v3h6v-3z"/></svg>
          <span>(02) 9415 6702</span>
        </li>
        <li class="contact-item group-gap">
          <svg class="contact-icon" viewBox="0 0 16 16"><path d="M8 1a7 7 0 100 14A7 7 0 008 1zm0 1.4c.7.8 1.3 2 1.5 3.1h-3C6.7 4.4 7.3 3.2 8 2.4zM2.5 9.5a5.6 5.6 0 010-3h2.6a11 11 0 000 3zm.6 1.4h2.2c.2 1 .6 1.9 1 2.7a5.6 5.6 0 01-3.2-2.7zm2.2-5.4H3.1a5.6 5.6 0 013.2-2.7c-.4.8-.8 1.7-1 2.7zM8 13.6c-.7-.8-1.3-1.9-1.5-2.7h3c-.2.8-.8 1.9-1.5 2.7zm1.7-4.1H6.3a9.6 9.6 0 010-3h3.4a9.6 9.6 0 010 3zm0 4.1c.4-.8.8-1.7 1-2.7h2.2a5.6 5.6 0 01-3.2 2.7zm1.2-4.1a11 11 0 000-3h2.6a5.6 5.6 0 010 3zm-.2-4c-.2-1-.6-1.9-1-2.7a5.6 5.6 0 013.2 2.7z"/></svg>
          <span>www.plovabuilding.com.au</span>
        </li>
        <li class="contact-item">
          <svg class="contact-icon" viewBox="0 0 16 16"><path d="M1 4h14v9H1zm1.5 1.2v.4L8 9.3l5.5-3.7v-.4zm0 2.1v4.5h11V7.3L8 11z"/></svg>
          <span>p.delvane@plovabuilding.com.au</span>
        </li>
        <li class="contact-item">
          <svg class="contact-icon" viewBox="0 0 16 16"><path d="M8 1a4.6 4.6 0 00-4.6 4.6C3.4 9 8 15 8 15s4.6-6 4.6-9.4A4.6 4.6 0 008 1zm0 6.4a1.8 1.8 0 110-3.6 1.8 1.8 0 010 3.6z"/></svg>
          <span>PO Box 87, Kelwyn NSW 2091</span>
        </li>
      </ul>
    </div>
    <div class="front-strip">
      <span class="brand-name">PLOVA</span>
    </div>
  </section>

  <section class="card card-back">
    <div class="back-band"></div>
    <div class="back-logo">
      <span class="brand-name">PLOVA</span>
      <p class="tagline">
        <span class="tagline-rule"></span>
        <span>Crestline Property Upgrades &amp; Refits</span>
        <span class="tagline-rule"></span>
      </p>
    </div>
    <p class="abn">ABN (71 903 257 146)</p>
  </section>

</div>
</body>
</html>
```